Update Business Card Design

I'm looking to update my business cards. Attached is a photo of the current design. I like the black side so that does not have to be update. The white side needs to be updated. I want the design to be modern and minimalistic.
I am a lawyer and my firm's website is www.harborstonepartners.com (for reference).
My firm's logo has a horizontal version (which is on the black side of the card) and a vertical version (on the white side). I would prefer to keep the vertical version on the white side and horizontal version on the black side (the logo files are attached).

I am open to redesigning the black side also. I would like one side to have the horizontal logo and the other to have the vertical logo.

Went on vacation/holiday

```html
<!DOCTYPE html>
<html lang="en">
<head>
<meta charset="utf-8">
<title>Harborstone Partners – Business Card</title>
<link rel="stylesheet" href="https://fonts.googleapis.com/css2?family=Montserrat:wght@400;500;600;700&display=swap">
<style>
  :root {
    --backdrop: #3a3a3c;
    --card-white: #ffffff;
    --card-dark: #282828;
    --brand-blue: #1bb3e0;
    --brand-grey: #5a5a5a;
    --ink: #1e1e1e;
    --paper-text: #ffffff;
  }
  * { box-sizing: border-box; margin: 0; padding: 0; }
  html, body {
    width: 1200px; height: 1200px; overflow: hidden;
    background: var(--backdrop);
  }
  .canvas {
    width: 1200px; height: 1200px;
    display: flex; flex-direction: column; align-items: center; justify-content: center;
    gap: 56px;
  }
  .card {
    position: relative;
    width: 900px; height: 514px;
    border-radius: 34px;
    overflow: hidden;
  }

  /* Front – white side */
  .card--front { background: var(--card-white); }
  .contact-block {
    position: absolute; left: 64px; top: 92px;
    font-family: "Montserrat", sans-serif; color: var(--ink);
  }
  .contact-block__name {
    font-size: 46px; font-weight: 700; color: var(--brand-blue); letter-spacing: 0.5px;
  }
  .contact-block__title {
    font-size: 21px; font-weight: 500; letter-spacing: 1px; text-transform: uppercase;
    margin-top: 4px;
  }
  .contact-list { list-style: none; margin-top: 22px; }
  .contact-list__item {
    display: flex; align-items: center; gap: 14px;
    font-size: 24px; font-weight: 400; line-height: 1; margin-bottom: 14px;
  }
  .contact-list__item:first-child { font-size: 22px; }
  .contact-list__icon { width: 26px; height: 26px; flex: none; }

  .brand-stack {
    position: absolute; right: 70px; top: 70px; width: 290px;
    display: flex; flex-direction: column; align-items: center; gap: 22px;
  }
  .brand-stack__mark {
    width: 120px; height: 120px; background: var(--brand-blue);
  }
  .brand-stack__name {
    font-family: "Montserrat", sans-serif; font-weight: 600; text-align: center;
    color: var(--brand-blue); font-size: 32px; line-height: 1.15; letter-spacing: 1px;
    text-transform: uppercase;
  }
  .address {
    position: absolute; left: 0; right: 40px; bottom: 66px;
    text-align: right;
    font-family: "Montserrat", sans-serif; font-size: 20px; font-weight: 500; color: var(--ink);
    letter-spacing: 0.3px;
  }
  .edge-band { position: absolute; left: 0; bottom: 0; width: 900px; height: 48px; }

  /* Back – dark side */
  .card--back {
    background: var(--card-dark);
    border-bottom: 4px solid var(--brand-blue);
  }
  .brand-line {
    position: absolute; left: 0; right: 0; top: 150px;
    display: flex; align-items: center; justify-content: center; gap: 34px;
  }
  .brand-line__mark { width: 130px; height: 130px; background: var(--brand-blue); flex: none; }
  .brand-line__name {
    font-family: "Montserrat", sans-serif; font-weight: 600; color: var(--brand-blue);
    font-size: 50px; line-height: 1.1; letter-spacing: 1px; text-transform: uppercase;
  }
  .website {
    position: absolute; left: 0; right: 0; bottom: 104px; text-align: center;
    font-family: "Montserrat", sans-serif; font-weight: 500; font-size: 24px; letter-spacing: 2px;
    color: var(--paper-text); text-transform: uppercase;
  }
</style>
</head>
<body>
<main class="canvas">

  <section class="card card--front" aria-label="Business card front">
    <div class="contact-block">
      <h1 class="contact-block__name">Daniel Mercer</h1>
      <p class="contact-block__title">Attorney at Law</p>
      <ul class="contact-list">
        <li class="contact-list__item">
          <svg class="contact-list__icon" viewBox="0 0 26 26" aria-hidden="true">
            <rect x="2" y="6" width="22" height="15" fill="var(--brand-blue)"/>
            <path d="M2 6 L13 15 L24 6" fill="none" stroke="#fff" stroke-width="2"/>
          </svg>
          daniel@HarborstonePartners.com
        </li>
        <li class="contact-list__item">
          <svg class="contact-list__icon" viewBox="0 0 26 26" aria-hidden="true">
            <rect x="7" y="2" width="12" height="22" rx="2" fill="none" stroke="var(--brand-blue)" stroke-width="2"/>
            <circle cx="13" cy="20" r="1.3" fill="var(--brand-blue)"/>
          </svg>
          310.555.0148
        </li>
        <li class="contact-list__item">
          <svg class="contact-list__icon" viewBox="0 0 26 26" aria-hidden="true">
            <path d="M6 3 L10 3 L12 9 L9 11 C10.5 14.5 12.5 16.5 16 18 L18 15 L24 17 L24 21 C24 22.5 22.5 24 21 24 C12 23 4 15 3 6 C3 4.5 4.5 3 6 3 Z" fill="var(--brand-blue)"/>
          </svg>
          310.555.0172
        </li>
        <li class="contact-list__item">
          <svg class="contact-list__icon" viewBox="0 0 26 26" aria-hidden="true">
            <rect x="8" y="2" width="12" height="8" fill="none" stroke="var(--brand-blue)" stroke-width="2"/>
            <rect x="2" y="9" width="22" height="15" rx="2" fill="var(--brand-blue)"/>
            <rect x="11" y="13" width="10" height="3" fill="#fff"/>
            <rect x="11" y="18" width="10" height="3" fill="#fff"/>
          </svg>
          310.555.0190
        </li>
      </ul>
    </div>

    <div class="brand-stack">
      <span class="brand-stack__mark" aria-hidden="true"></span>
      <p class="brand-stack__name">Harborstone<br>Partners</p>
    </div>

    <p class="address">1180 Westview Avenue, Suite 310, Fairmont, CA 90000</p>

    <svg class="edge-band" viewBox="0 0 900 48" preserveAspectRatio="none" aria-hidden="true">
      <polygon points="0,24 560,24 548,48 0,48" fill="var(--brand-blue)"/>
      <polygon points="572,0 900,0 900,48 560,48" fill="var(--brand-grey)"/>
    </svg>
  </section>

  <section class="card card--back" aria-label="Business card back">
    <div class="brand-line">
      <span class="brand-line__mark" aria-hidden="true"></span>
      <p class="brand-line__name">Harborstone<br>Partners</p>
    </div>
    <p class="website">www.harborstonepartners.com</p>
  </section>

</main>
</body>
</html>
```